I have a gravoni sauce and I want a label made with this logo. Gravoni is buffalo sauce with truffles added to it to enhance the flavor. I provided a photo so you know what color you have to work with. I'd like the logo provided on a fun or crazy background that goes well with the sauce color. Thanks

Logo Text

Dellmont Harvick Gravoni Sauce

Requirements
Must have
• Must have my logo that I provided.

```html
<!DOCTYPE html>
<html lang="en">
<head>
<meta charset="utf-8">
<title>Dellmont Harvick Gravoni Sauce – Label Options</title>
<link href="https://fonts.googleapis.com/css2?family=Oswald:wght@500;700&display=swap" rel="stylesheet">
<style>
  :root {
    --backdrop: #8f1a1f;
    --flame-yellow: #ffe600;
    --flame-gold: #ffc21a;
    --flame-orange: #f28a1c;
    --cream: #ffffff;
    --brand-red: #d1202a;
    --sauce-orange: #ea6a1f;
    --rim-yellow: #ffe000;
  }
  * { margin: 0; padding: 0; box-sizing: border-box; }
  html, body { width: 1200px; height: 1200px; overflow: hidden; }
  body {
    background: var(--backdrop);
    font-family: "Oswald", sans-serif;
    display: flex;
    align-items: center;
    justify-content: center;
    gap: 70px;
  }
  .label {
    position: relative;
    width: 440px;
    height: 620px;
    border-radius: 64px;
    overflow: hidden;
  }
  .label__art { position: absolute; inset: 0; width: 100%; height: 100%; }
  .brand {
    position: absolute;
    left: 0; right: 0;
    top: 150px;
    text-align: center;
    color: var(--brand-red);
    font-weight: 700;
    line-height: 0.95;
    text-transform: uppercase;
  }
  .brand__first { display: block; font-size: 48px; letter-spacing: 10px; }
  .brand__last { display: block; font-size: 96px; letter-spacing: 2px; }
  .product {
    position: absolute;
    left: 0; right: 0;
    text-align: center;
    font-weight: 500;
    text-transform: uppercase;
    line-height: 1;
  }
  .product__name { display: block; color: var(--sauce-orange); font-size: 64px; }
  .product__type { display: block; color: var(--brand-red); font-size: 64px; }
  .label--diagonal .product { top: 360px; transform: rotate(-15deg); }
  .label--classic .product { top: 410px; }
  .label--classic { border: 8px solid var(--rim-yellow); border-top: none; }
</style>
</head>
<body>

  <section class="label label--diagonal">
    <svg class="label__art" viewBox="0 0 440 620" role="img" aria-label="Fiery yellow and orange cloud texture with a diagonal white band">
      <defs>
        <linearGradient id="flameDiagonal" x1="0.2" y1="0" x2="0.55" y2="1">
          <stop offset="0" stop-color="var(--flame-orange)"/>
          <stop offset="0.18" stop-color="var(--flame-gold)"/>
          <stop offset="0.4" stop-color="var(--flame-yellow)"/>
          <stop offset="0.55" stop-color="var(--cream)"/>
          <stop offset="0.74" stop-color="var(--cream)"/>
          <stop offset="0.86" stop-color="var(--flame-yellow)"/>
          <stop offset="1" stop-color="var(--flame-orange)"/>
        </linearGradient>
      </defs>
      <rect width="440" height="620" fill="url(#flameDiagonal)"/>
    </svg>
    <h1 class="brand"><span class="brand__first">Dellmont</span><span class="brand__last">Harvick</span></h1>
    <p class="product"><span class="product__name">Gravoni</span><span class="product__type">Sauce</span></p>
  </section>

  <section class="label label--classic">
    <svg class="label__art" viewBox="0 0 440 620" preserveAspectRatio="none" role="img" aria-label="Fiery yellow and orange cloud texture fading into a white lower panel">
      <defs>
        <linearGradient id="flameVertical" x1="0" y1="0" x2="0" y2="1">
          <stop offset="0" stop-color="var(--flame-orange)"/>
          <stop offset="0.2" stop-color="var(--flame-gold)"/>
          <stop offset="0.45" stop-color="var(--flame-yellow)"/>
          <stop offset="0.58" stop-color="var(--cream)"/>
          <stop offset="1" stop-color="var(--cream)"/>
        </linearGradient>
      </defs>
      <rect width="440" height="620" fill="url(#flameVertical)"/>
    </svg>
    <h2 class="brand"><span class="brand__first">Dellmont</span><span class="brand__last">Harvick</span></h2>
    <p class="product"><span class="product__name">Gravoni</span><span class="product__type">Sauce</span></p>
  </section>

</body>
</html>
```